Embroidery Teacher

I design and teach small embroidery classes, I am based in South Australia
The majority of my embroidery is done on bright wool fabrics and the designs are naive / folk art type birds, flowers and houses. The finished products stitched by the ladies in my classes are usually made into book covers, needle keepers or small quilts.

Industry/Entity Type

Embroidery

Contact Information for Business Card

Rosalind Hatchett
PO Box 3817
Fernvale SA 5092
M. 0427183592
E. ros@merrythreadwork.com.au

```html
<!DOCTYPE html>
<html lang="en">
<head>
<meta charset="utf-8">
<title>Rosalind Hatchett – Business Card</title>
<link rel="stylesheet" href="https://fonts.googleapis.com/css2?family=Andika:wght@400;700&display=swap">
<style>
  :root {
    --page: #ebebec;
    --linen: #c8bea6;
    --linen-light: #d6cdb6;
    --glow: #e4dc7a;
    --thread: #e2b628;
    --thread-shadow: #8a7a55;
    --ink-yellow: #dccb08;
  }
  html, body {
    margin: 0;
    width: 1200px;
    height: 800px;
    overflow: hidden;
    background: var(--page);
  }
  .canvas {
    position: relative;
    width: 1200px;
    height: 800px;
    display: flex;
    align-items: center;
    justify-content: center;
    gap: 60px;
  }
  .card {
    width: 520px;
    height: 289px;
    display: block;
    box-shadow: 0 4px 14px rgba(0,0,0,0.18);
  }
  .card-name-mark {
    font-family: "Andika", sans-serif;
    font-weight: 700;
    font-size: 46px;
    fill: var(--thread);
  }
  .card-detail {
    font-family: "Andika", sans-serif;
    font-weight: 700;
    font-size: 19px;
    fill: var(--ink-yellow);
  }
  .stitch {
    fill: none;
    stroke: var(--thread);
    stroke-width: 2;
    stroke-dasharray: 7 4;
  }
  .seam {
    fill: none;
    stroke: var(--thread-shadow);
    stroke-width: 1;
    opacity: 0.45;
  }
</style>
</head>
<body>
<main class="canvas">

  <!-- Front of card -->
  <svg class="card card-front" viewBox="0 0 520 289" aria-label="Business card front">
    <defs>
      <radialGradient id="frontGlow" cx="0.3" cy="0.3" r="0.9">
        <stop offset="0" stop-color="var(--glow)" stop-opacity="0.55"/>
        <stop offset="0.6" stop-color="var(--linen-light)" stop-opacity="0.2"/>
        <stop offset="1" stop-color="var(--linen)" stop-opacity="0"/>
      </radialGradient>
    </defs>
    <rect class="card-base" width="520" height="289" fill="var(--linen)"/>
    <rect width="520" height="289" fill="url(#frontGlow)"/>
    <rect class="seam" x="20" y="20" width="480" height="249"/>
    <rect class="stitch" x="16" y="16" width="488" height="257"/>
    <text class="card-name-mark" x="260" y="150" text-anchor="middle">Rosalind Hatchett</text>
    <line x1="60" y1="178" x2="470" y2="190" stroke="var(--thread)" stroke-width="6" stroke-linecap="round"/>
  </svg>

  <!-- Back of card -->
  <svg class="card card-back" viewBox="0 0 520 289" aria-label="Business card back">
    <defs>
      <radialGradient id="backGlow" cx="0.2" cy="0.5" r="0.8">
        <stop offset="0" stop-color="var(--glow)" stop-opacity="0.85"/>
        <stop offset="0.7" stop-color="var(--linen-light)" stop-opacity="0.3"/>
        <stop offset="1" stop-color="var(--linen)" stop-opacity="0"/>
      </radialGradient>
    </defs>
    <rect class="card-base" width="520" height="289" fill="var(--linen)"/>
    <rect width="520" height="289" fill="url(#backGlow)"/>
    <rect class="stitch" x="12" y="12" width="496" height="265"/>
    <path class="stitch" d="M230 12 L508 150"/>
    <path class="stitch" d="M290 12 L508 118"/>
    <path class="seam" d="M234 16 L504 152"/>
    <text class="card-detail" x="30" y="96">Rosalind Hatchett</text>
    <text class="card-detail" x="30" y="126">PO Box 3817</text>
    <text class="card-detail" x="30" y="156">Fernvale SA 5092</text>
    <text class="card-detail" x="30" y="186">M. 0427183592</text>
    <text class="card-detail" x="30" y="216">E. ros@merrythreadwork.com.au</text>
    <text class="card-detail" x="30" y="256">merrythreadwork.com.au</text>
  </svg>

</main>
</body>
</html>
```